Letterhead and Stationary for Construction Company

Brisk Current needs modern Letterhead, Envelopes and Notepad designs.

Industry/Entity Type

Construction

Colors
f78f20
34a7d8
ffffff

Requirements
Must have
• Modern looking design.

```html
<!DOCTYPE html>
<html lang="en">
<head>
<meta charset="utf-8">
<title>Brisk Current – Stationery</title>
<link href="https://fonts.googleapis.com/css2?family=Open+Sans:wght@400;600;700&display=swap" rel="stylesheet">
<style>
  :root {
    --brand-orange: #f07d1f;
    --brand-blue: #2f68ad;
    --flap-blue: #3a73b8;
    --paper: #ffffff;
    --paper-shade: #f3f4f6;
    --fold-line: #e1e3e7;
    --ink-grey: #6b6f76;
    --backdrop: #e6eaf0;
  }
  html, body {
    margin: 0;
    width: 1200px;
    height: 950px;
    overflow: hidden;
    background: var(--backdrop);
    font-family: "Open Sans", sans-serif;
  }
  .stationery-set {
    position: relative;
    width: 1200px;
    height: 950px;
  }
  .sheet {
    position: absolute;
    left: 170px;
    width: 860px;
    height: 430px;
    background: var(--paper);
    box-shadow: 0 6px 18px rgba(30, 50, 80, 0.18);
  }
  .letterhead { top: 30px; }
  .envelope { top: 490px; background: var(--paper-shade); }
  .sheet svg { display: block; width: 100%; height: 100%; }
  .wordmark { font-family: "Open Sans", sans-serif; font-weight: 600; fill: var(--brand-orange); }
  .contact-text { font-family: "Open Sans", sans-serif; font-size: 10px; fill: var(--ink-grey); }
  .web-address { font-family: "Open Sans", sans-serif; font-weight: 700; font-size: 14px; fill: #fff; }
</style>
</head>
<body>
<main class="stationery-set">

  <section class="sheet letterhead" aria-label="Brisk Current letterhead">
    <svg viewBox="0 0 860 430" xmlns="http://www.w3.org/2000/svg">
      <!-- header -->
      <line class="header-rule-left" x1="0" y1="80" x2="56" y2="80" stroke="var(--brand-orange)" stroke-width="4"/>
      <circle class="brand-dot" cx="70" cy="75" r="8" fill="var(--brand-orange)"/>
      <text class="wordmark" x="84" y="84" font-size="24">brisk current</text>
      <line class="header-rule-right" x1="250" y1="70" x2="860" y2="70" stroke="var(--brand-blue)" stroke-width="5"/>

      <!-- footer contact row -->
      <g class="contact-row">
        <circle cx="26" cy="394" r="5" fill="var(--brand-blue)"/>
        <circle cx="26" cy="394" r="1.8" fill="#fff"/>
        <text class="contact-text" x="36" y="398">00 Mill Lane, Harrowgate Fields HG 00 0RT</text>

        <circle cx="274" cy="394" r="5" fill="var(--brand-blue)"/>
        <rect x="271.5" y="391" width="5" height="6" rx="1" fill="#fff"/>
        <text class="contact-text" x="284" y="398">(01632) 960 418</text>

        <circle cx="378" cy="394" r="5" fill="var(--brand-blue)"/>
        <rect x="375.5" y="391" width="5" height="6" rx="1" fill="#fff"/>
        <text class="contact-text" x="388" y="398">(01632) 960 927</text>

        <circle cx="482" cy="394" r="5" fill="var(--brand-blue)"/>
        <rect x="479" y="391.5" width="6" height="5" fill="#fff"/>
        <text class="contact-text" x="492" y="398">contact@briskcurrent.com</text>
      </g>

      <!-- footer stripes -->
      <polygon class="stripe-orange" points="0,408 188,408 184,414 0,414" fill="var(--brand-orange)"/>
      <polygon class="stripe-blue" points="194,408 400,408 396,414 190,414" fill="var(--brand-blue)"/>
      <polygon class="stripe-orange" points="406,408 630,408 626,414 402,414" fill="var(--brand-orange)"/>
      <rect class="base-band" x="0" y="419" width="860" height="11" fill="var(--brand-blue)"/>
      <polygon class="web-tab" points="638,430 652,384 860,384 860,430" fill="var(--brand-blue)"/>
      <text class="web-address" x="846" y="413" text-anchor="end">www.briskcurrent.com</text>
    </svg>
  </section>

  <section class="sheet envelope" aria-label="Brisk Current envelope, back">
    <svg viewBox="0 0 860 430" xmlns="http://www.w3.org/2000/svg">
      <!-- fold lines of the envelope body -->
      <path class="fold-lines" d="M20,430 L60,170 Q64,150 90,148 M840,430 L800,120 Q796,104 770,104" fill="none" stroke="var(--fold-line)" stroke-width="2"/>
      <!-- opened flap lining -->
      <path class="flap-lining" role="img" aria-label="Envelope flap lining with a repeating blue geometric pattern"
            d="M0,0 H860 V40 Q858,62 830,64 L740,68 Q700,70 680,95 L420,120 L120,120 Q60,120 40,150 L0,170 Z"
            fill="var(--flap-blue)"/>
      <!-- brand name -->
      <circle class="brand-dot" cx="560" cy="236" r="11" fill="var(--brand-orange)"/>
      <text class="wordmark" x="578" y="248" font-size="32">brisk current</text>
    </svg>
  </section>

</main>
</body>
</html>
```